Stationary Design for Stunning new Logo

I need to envelopes, letterhead, business cards designed to compliment our new logo.

We are a 25 year old printing company going through a brand refresh. All items should have the design extended to both sides for full print ability.

Industry/Entity Type

Printing

Requirements
Must have
• It must utilize the new logo & colors PMS 300 & PMS 295.

```html
<!DOCTYPE html>
<html lang="en">
<head>
<meta charset="utf-8">
<title>Printora Stationery Set</title>
<link href="https://fonts.googleapis.com/css2?family=Roboto+Slab:wght@400;700&display=swap" rel="stylesheet">
<style>
  :root {
    --pms-300: #0077c8;
    --pms-295: #0b3f7a;
    --paper: #ffffff;
    --backdrop: #e6e6e4;
    --ink-soft: #4a6f99;
    --ink-muted: #777777;
  }
  * { box-sizing: border-box; margin: 0; padding: 0; }
  html, body { width: 1200px; height: 1000px; overflow: hidden; }
  body {
    background: var(--backdrop);
    position: relative;
    font-family: "Roboto Slab", Georgia, serif;
    color: var(--pms-295);
  }
  .sheet {
    position: absolute;
    background: var(--paper);
    box-shadow: 0 6px 18px rgba(0,0,0,.18);
  }
  .brand {
    font-family: "Roboto Slab", Georgia, serif;
    font-weight: 700;
    color: var(--pms-295);
    letter-spacing: 1px;
    line-height: 1;
    display: flex;
    align-items: center;
    white-space: nowrap;
  }
  .brand-dot {
    display: inline-block;
    border-radius: 50%;
    background: var(--pms-300);
    flex: none;
  }

  /* Letterhead */
  .letterhead { left: 148px; top: 104px; width: 612px; height: 791px; }
  .letterhead .masthead { position: absolute; top: 48px; left: 0; right: 0; display: flex; justify-content: center; }
  .letterhead .brand { font-size: 36px; gap: 10px; }
  .letterhead .brand-dot { width: 34px; height: 34px; }
  .letterhead .footer-band {
    position: absolute; left: 0; right: 0; bottom: 0; height: 61px;
    background: var(--pms-300); color: #fff;
    display: flex; align-items: center; padding-left: 44px;
    font-size: 11px; font-weight: 700; letter-spacing: .6px; white-space: nowrap;
  }
  .sep { margin: 0 6px; font-size: 8px; }

  /* Envelope */
  .envelope { left: 368px; top: 500px; width: 684px; height: 296px; }
  .envelope .return { position: absolute; left: 27px; top: 24px; }
  .envelope .brand { font-size: 19px; gap: 6px; }
  .envelope .brand-dot { width: 18px; height: 18px; }
  .envelope .return-address { font-size: 6.5px; color: var(--ink-soft); margin: 5px 0 0 24px; white-space: nowrap; }

  /* Business cards */
  .card { left: 797px; width: 252px; height: 143px; }
  .card-front { top: 150px; }
  .card-front .brand-block { position: absolute; left: 15px; top: 16px; }
  .card-front .brand { font-size: 21px; gap: 6px; }
  .card-front .brand-dot { width: 22px; height: 22px; }
  .contact-person { position: absolute; left: 18px; top: 63px; font-size: 8px; line-height: 1.3; white-space: nowrap; }
  .contact-person .name { font-weight: 700; font-size: 10px; letter-spacing: .6px; text-transform: uppercase; }
  .contact-person .title { font-size: 5.5px; color: var(--ink-muted); text-transform: uppercase; margin-bottom: 3px; }
  .contact-person .email { font-style: italic; color: var(--pms-300); }
  .contact-office { position: absolute; right: 18px; top: 63px; text-align: right; font-size: 8px; line-height: 1.34; white-space: nowrap; }
  .label { color: var(--pms-300); }
  .card-front .web-band {
    position: absolute; left: 0; right: 0; bottom: 0; height: 26px;
    background: var(--pms-300); color: #fff;
    display: flex; align-items: center; justify-content: center;
    font-size: 10px; font-weight: 700; letter-spacing: 1px;
  }
  .card-back { top: 323px; display: flex; align-items: center; justify-content: center; }
  .card-back .brand { font-size: 22px; gap: 8px; }
  .card-back .brand-dot { width: 22px; height: 22px; }
</style>
</head>
<body>

  <section class="sheet letterhead" aria-label="Letterhead">
    <header class="masthead">
      <div class="brand"><span class="brand-dot"></span>PRINTORA</div>
    </header>
    <footer class="footer-band">
      48 Harbor Lane, Millbrook, ST 20418<span class="sep">■</span>p 555.214.3380<span class="sep">■</span>f 555.214.3381<span class="sep">■</span>www.printora.com
    </footer>
  </section>

  <section class="sheet envelope" aria-label="Envelope">
    <div class="return">
      <div class="brand"><span class="brand-dot"></span>PRINTORA</div>
      <div class="return-address">48 Harbor Lane, Millbrook, ST 20418</div>
    </div>
  </section>

  <section class="sheet card card-front" aria-label="Business card front">
    <div class="brand-block">
      <div class="brand"><span class="brand-dot"></span>PRINTORA</div>
    </div>
    <div class="contact-person">
      <div class="name">Dana Morrow</div>
      <div class="title">President</div>
      <div class="email">dmorrow@printora.com</div>
      <div><span class="label">mobile</span> 555.867.0912</div>
    </div>
    <div class="contact-office">
      <div><span class="label">office</span> 555.214.3380</div>
      <div><span class="label">fax</span> 555.214.3381</div>
      <div>48 Harbor Lane</div>
      <div>Millbrook, ST 20418</div>
    </div>
    <div class="web-band">www.printora.com</div>
  </section>

  <section class="sheet card card-back" aria-label="Business card back">
    <div class="brand"><span class="brand-dot"></span>PRINTORA</div>
  </section>

</body>
</html>
```